Book Title: The Harbor's Lantern. Author Name: Marisol Thackeray

We are needing a cover, spine and back cover design for a poetry book that we are publishing called The Harbor's Lantern. We are looking for an elegant, and simplistic design with a very natural, dynamic and powerful impact.

Design Idea #1 - Shiva Conch Shell with a pink or black background. See Glen Parvey Image attached for design inspiration. Simple and dynamic .
Title and Author name created in same style as the attached Glen Parvey's Lanterns and Driftwood image.

Design Idea #2 - Image of cauldron on (see cauldrons attached for ideas) black background.
See Glen Parvey Image attached for design inspiration. Simple and dynamic Title and Author name created in same style as the attached Glen Parvey's Lanterns and Driftwood image

Design Idea #3 - Image of Tree of Life (see attached images for idea of what we are looking for) Would like to see on plain white, green, black and green background.

Target Market(s)

Spiritual Women, healers, visionaries,Goddess'

Requirements
Must have
• Please see project descriptions for specific design concepts we are looking for. Please include the authors name: Marisol Thackeray on front, spine and back cover of the book

```html
<!DOCTYPE html>
<html lang="en">
<head>
<meta charset="utf-8">
<title>The Harbor's Lantern — Marisol Thackeray</title>
<link rel="stylesheet" href="https://fonts.googleapis.com/css2?family=Marcellus&display=swap">
<style>
  :root {
    --cover-black: #000000;
    --author-cream: #f1e6da;
    --title-pink: #ebc3c8;
    --art-teal: #3d95b5;
    --art-rose: #e39a93;
    --art-violet: #6e4c8f;
    --art-lime: #d8e79a;
  }
  html, body {
    margin: 0;
    padding: 0;
    width: 750px;
    height: 1200px;
    overflow: hidden;
    background: var(--cover-black);
  }
  .cover {
    position: relative;
    width: 750px;
    height: 1200px;
    background: var(--cover-black);
    font-family: "Marcellus", "Times New Roman", serif;
    text-transform: uppercase;
    text-align: center;
  }
  .author {
    position: absolute;
    top: 92px;
    left: 0;
    width: 100%;
    margin: 0;
    color: var(--author-cream);
    font-weight: 400;
    line-height: 1;
  }
  .author-first {
    display: block;
    font-size: 54px;
    letter-spacing: 1px;
  }
  .author-last {
    display: block;
    margin-top: 26px;
    font-size: 72px;
    letter-spacing: 0.5px;
  }
  .tree-art {
    position: absolute;
    left: 155px;
    top: 335px;
    width: 440px;
    height: 440px;
  }
  .title {
    position: absolute;
    top: 832px;
    left: 0;
    width: 100%;
    margin: 0;
    color: var(--title-pink);
    font-weight: 400;
    font-size: 100px;
    line-height: 91px;
    letter-spacing: 0;
  }
  .title span { display: block; }
</style>
</head>
<body>
  <main class="cover">
    <h2 class="author">
      <span class="author-first">Marisol</span>
      <span class="author-last">Thackeray</span>
    </h2>

    <svg class="tree-art" viewBox="0 0 440 440" role="img" aria-label="Circular tree of life illustration with intertwined branches, leaves and roots in iridescent pastel colours">
      <defs>
        <radialGradient id="treeTones" cx="50%" cy="55%" r="55%">
          <stop offset="0%" stop-color="var(--art-teal)"/>
          <stop offset="45%" stop-color="var(--art-violet)"/>
          <stop offset="75%" stop-color="var(--art-rose)"/>
          <stop offset="100%" stop-color="var(--art-lime)"/>
        </radialGradient>
      </defs>
      <circle cx="220" cy="220" r="218" fill="url(#treeTones)"/>
    </svg>

    <h1 class="title">
      <span>The</span>
      <span>Harbor's</span>
      <span>Lantern</span>
    </h1>
  </main>
</body>
</html>
```